Dog care service needs advertising poster

Our company is Paw Haven. We provide care for dogs while their owners are away, either through home visits or a holiday stay in the homes of carefully selected minders. Our existing website & Facebook cover should provide all the colour cues for a poster - namely blues, blondes and grey. We have an existing logo (provided). We can feature the same imagery from our website as I have purchased the rights to the stock images.

www.pawhavenexample.com.au
www.facebook.com/pawhavenexampleau

This brief is for design of a poster that can be placed in vet surgeries, groomers, on community noticeboards. It should be scalable to print in three sizes, A5, A4 & A3.

We wish to clearly communicate our three areas of service "dog minding, home visits, dog walking".

We would like to have the files ready for upload to Printora (or similar) for immediate printing.

Target Market(s)

Dog owners who love their dogs like family.

Industry/Entity Type

Advertising

Font styles to use
Sans Serif

Colors
33a6d7
3276b5

Requirements
Must have
• Logo
• www.pawhavenexample.com.au
• Telephone number
• Three services - Dog Minding, Home Visits, Dog Walking
Nice to have
• use of our existing stock photography to highlight the three areas of service - Dog minding, home visits, dog walking. Existing colour palette - blues, blondes and grey.
• Text that can be used:
• Western Sydney’s complete dog care service.
• Dog Minding - Your dog stays in the home of one of our carefully selected minders.Treated like part of the family, they enjoy all the creature comforts they are used to.
• Home Visits - We visit your dog at your home for feeding, walking and playtime. Short of long visits available.
• Dog Walking - If you can't walk your dog for any reason we are here to help. 1/2 hour or hourly walks available.
• Contact us today for a tailored package to meet your needs.
Should not have
• Any additional illustrations beyond the logo.

```html
<!DOCTYPE html>
<html lang="en">
<head>
<meta charset="utf-8">
<title>Paw Haven – Dog Care Poster</title>
<link rel="stylesheet" href="https://fonts.googleapis.com/css2?family=Archivo+Black&family=Hind:wght@500;600&family=Tinos&display=swap">
<style>
  :root {
    --page: #ffffff;
    --brand-blue: #3a87e8;
    --band-light: #dcEFF9;
    --navy: #2d3e56;
    --leash-brown: #8a4a2c;
    --sky: #bfe3f6;
    --grass: #3fae1e;
    --grass-dark: #2d8f12;
    --white: #ffffff;
  }
  * { margin: 0; padding: 0; box-sizing: border-box; }
  html, body { width: 1000px; height: 1200px; overflow: hidden; background: var(--page); }
  .poster {
    position: absolute; left: 92px; top: 22px; width: 816px; height: 1156px;
    background: var(--white); overflow: hidden;
    box-shadow: 0 2px 10px rgba(0,0,0,0.35);
  }
  .top-band { position: absolute; left: 0; top: 0; width: 100%; height: 23px; background: var(--brand-blue); }
  .top-band::after { content: ""; position: absolute; left: 0; bottom: -5px; width: 100%; height: 2px; background: var(--band-light); }
  .brand {
    position: absolute; left: 0; top: 23px; width: 100%; height: 205px;
    display: flex; align-items: center; justify-content: center; gap: 22px;
  }
  .brand-dot { width: 70px; height: 70px; border-radius: 50%; background: var(--navy); }
  .brand-name {
    font-family: "Hind", sans-serif; font-weight: 600; font-size: 82px;
    color: var(--navy); line-height: 1; padding-top: 14px;
  }
  .divider-band { position: absolute; left: 0; top: 228px; width: 100%; height: 15px; background: var(--band-light); }
  .headline { position: absolute; left: 0; top: 250px; width: 100%; height: 90px; }
  .headline text {
    font-family: "Archivo Black", sans-serif; font-size: 76px;
    fill: var(--white); stroke: var(--brand-blue); stroke-width: 16px;
    stroke-linejoin: round; paint-order: stroke fill;
  }
  .scene {
    position: absolute; left: 0; top: 640px; width: 100%; height: 463px;
    background: linear-gradient(to bottom, #ffffff 0%, #ffffff 8%, var(--sky) 45%, #e6f4fa 58%, var(--grass) 72%, var(--grass-dark) 100%);
  }
  .scene-subject {
    position: absolute; left: 28px; top: 60px; width: 350px; height: 400px;
    border-radius: 40% 40% 12% 12%; background: linear-gradient(#e7d5bd, #d9c2a2);
  }
  .leash { position: absolute; left: 0; top: 0; width: 816px; height: 1156px; pointer-events: none; }
  .services-box {
    position: absolute; left: 180px; top: 353px; width: 583px; height: 293px;
    border: 7px solid var(--leash-brown); border-radius: 18px; background: var(--white);
    display: flex; flex-direction: column; justify-content: center; align-items: flex-end;
    padding-right: 40px;
  }
  .service {
    font-family: "Hind", sans-serif; font-weight: 600; font-size: 80px;
    color: var(--brand-blue); line-height: 90px; letter-spacing: 1px;
  }
  .phone { position: absolute; left: 326px; top: 920px; display: flex; align-items: center; gap: 14px; }
  .phone-icon { width: 62px; height: 58px; }
  .phone-number {
    font-family: "Archivo Black", sans-serif; font-size: 46px; color: var(--white);
    text-shadow: 2px 3px 4px rgba(0,0,0,0.55); letter-spacing: 1px;
  }
  .footer-band {
    position: absolute; left: 0; top: 1103px; width: 100%; height: 53px;
    background: var(--brand-blue); border-top: 4px solid #9cc8f2;
    display: flex; align-items: center; justify-content: center;
  }
  .website { font-family: "Tinos", serif; font-size: 31px; color: var(--white); }
</style>
</head>
<body>
<main class="poster">
  <div class="top-band"></div>

  <header class="brand">
    <span class="brand-dot"></span>
    <span class="brand-name">Paw Haven</span>
  </header>
  <div class="divider-band"></div>

  <svg class="headline" viewBox="0 0 816 90">
    <text x="408" y="75" text-anchor="middle">THREE SERVICES</text>
  </svg>

  <div class="scene" role="img" aria-label="Photo of an English bulldog on a brown leash standing on green grass under a pale blue sky">
    <div class="scene-subject"></div>
  </div>

  <svg class="leash" viewBox="0 0 816 1156">
    <line x1="760" y1="642" x2="320" y2="722" stroke="var(--leash-brown)" stroke-width="7" stroke-linecap="round"/>
  </svg>

  <section class="services-box">
    <p class="service">Dog Minding</p>
    <p class="service">Home Visits</p>
    <p class="service">Dog Walking</p>
  </section>

  <div class="phone">
    <svg class="phone-icon" viewBox="0 0 62 58">
      <rect x="2" y="2" width="58" height="54" rx="10" fill="var(--brand-blue)" stroke="#1f5fae" stroke-width="3"/>
      <rect x="11" y="9" width="40" height="40" rx="6" fill="#8fd3f3"/>
      <path d="M24 17c-2 1-4 3-3 7 2 7 7 13 13 16 3 1 5 0 7-2l-4-5-3 2c-3-2-6-6-7-9l2-3z" fill="var(--white)"/>
    </svg>
    <span class="phone-number">0400 555 123</span>
  </div>

  <footer class="footer-band">
    <span class="website">www.pawhavenexample.com.au</span>
  </footer>
</main>
</body>
</html>
```